Package Design for Chew Bone Guild for Marketora

Would like a label to put on a 6x9 package.

Here is my site: chewboneguild.example

Here are the labels I like:
https://rolfandkit.example/collections/bully-sticks/products/6-inch-standard-bully-sticks
https://www.marketora.example/stores/Rolf+%26+Kit/page/A1B2C3D4-5E6F-47A8-9B0C-1D2E3F4A5B6C?ref_=ast_bln
https://quiet-meadowland.example/amber-hound-junior-bully-sticks-6-25-pack/
https://www.wagsandwhimsy.example/shop/open-trailer-bully-stix

```html
<!DOCTYPE html>
<html lang="en">
<head>
<meta charset="utf-8">
<title>Chew Bone Guild – Bully Sticks Label</title>
<link href="https://fonts.googleapis.com/css2?family=Montserrat:wght@500;600;700;800;900&display=swap" rel="stylesheet">
<style>
  :root {
    --stage: #eeeeee;
    --label: #f4f4f4;
    --band: #a9cf9b;
    --blob: #b9d9ad;
    --green-dark: #3d8a1f;
    --green-bright: #5aa52b;
    --ink: #1c1c1c;
    --rule: #2a2a2a;
    --stick: #8a4a22;
    --stick-light: #b8703a;
    --dog-dark: #3a2e28;
    --dog-mid: #8a7260;
    --dog-light: #dccbb4;
  }
  * { margin: 0; padding: 0; box-sizing: border-box; }
  html, body { width: 1180px; height: 1200px; overflow: hidden; background: var(--stage); }
  body { font-family: "Montserrat", sans-serif; color: var(--ink); }

  .label {
    position: absolute; left: 210px; top: 0;
    width: 760px; height: 1200px;
    background: var(--label);
    overflow: hidden;
  }
  .brand-band {
    position: absolute; left: 195px; top: 0;
    width: 365px; height: 530px;
    background: var(--band);
    border-radius: 0 0 182px 182px;
  }
  .brand-seal {
    position: absolute; left: 220px; top: 175px;
    width: 310px; height: 310px;
    border-radius: 50%;
    background: #fff;
    border: 7px solid var(--ink);
    display: flex; align-items: center; justify-content: center;
    text-align: center;
  }
  .brand-name {
    font-weight: 800; font-size: 34px; line-height: 1.15;
    letter-spacing: 2px; text-transform: uppercase; color: var(--ink);
  }
  .blob {
    position: absolute; left: 340px; top: 790px;
    width: 520px; height: 460px;
  }
  .tagline {
    position: absolute; left: 63px; top: 568px;
    font-weight: 600; font-size: 23px; letter-spacing: 7px; white-space: nowrap;
  }
  .title-main {
    position: absolute; left: 60px; top: 592px;
    font-weight: 900; font-size: 128px; line-height: 1;
    color: var(--green-dark); letter-spacing: -4px; white-space: nowrap;
  }
  .title-sub {
    position: absolute; left: 66px; top: 714px;
    font-weight: 900; font-size: 60px; line-height: 1;
    color: var(--green-bright); letter-spacing: -1px; white-space: nowrap;
  }
  .title-tag {
    position: absolute; left: 302px; top: 718px;
    padding: 8px 14px;
    background: var(--ink); color: #fff;
    font-weight: 500; font-size: 22px; line-height: 1.05; white-space: nowrap;
  }
  .sticks-art {
    position: absolute; left: 81px; top: 800px;
    width: 324px; height: 125px;
  }
  .dogs-photo {
    position: absolute; left: 448px; top: 646px;
    width: 250px; height: 512px;
  }
  .features {
    position: absolute; left: 40px; top: 952px;
    list-style: none; width: 290px;
  }
  .features li {
    font-weight: 700; font-size: 20px; text-transform: uppercase;
    padding: 5px 0 7px 32px;
    border-bottom: 2px solid var(--rule);
    position: relative; white-space: nowrap;
  }
  .features li::before {
    content: "•"; position: absolute; left: 18px; top: 4px;
  }
  .size-note {
    position: absolute; left: 80px; top: 1110px;
    display: flex; align-items: flex-end; gap: 4px;
  }
  .size-num { font-weight: 900; font-size: 46px; line-height: 1; }
  .size-text { font-weight: 800; font-size: 19px; line-height: 0.95; text-transform: uppercase; padding-bottom: 2px; }
</style>
</head>
<body>
  <main class="label">
    <div class="brand-band"></div>
    <div class="brand-seal"><span class="brand-name">Chew<br>Bone<br>Guild</span></div>

    <svg class="blob" viewBox="0 0 520 460" aria-hidden="true">
      <path d="M400 20 C460 10 500 60 500 120 L500 460 L120 460 C40 440 0 360 40 290 C80 220 200 240 250 170 C290 110 330 30 400 20 Z" fill="var(--blob)"/>
    </svg>

    <p class="tagline">NATURALLY ODOR FREE</p>
    <h1 class="title-main">BULLY</h1>
    <p class="title-sub">STICKS</p>
    <p class="title-tag">PREMIUM<br>DOG CHEWS</p>

    <div class="sticks-art" role="img" aria-label="Photo of three brown bully sticks crossed">
      <svg width="324" height="125" viewBox="0 0 324 125">
        <defs>
          <linearGradient id="stickTone" x1="0" x2="1">
            <stop offset="0" stop-color="var(--stick)"/>
            <stop offset="1" stop-color="var(--stick-light)"/>
          </linearGradient>
        </defs>
        <rect x="0" y="40" width="324" height="50" rx="25" fill="url(#stickTone)" opacity="0.85"/>
      </svg>
    </div>

    <div class="dogs-photo" role="img" aria-label="Photo of a pug in sunglasses and bandana sitting beside a tricolour mountain dog">
      <svg width="250" height="512" viewBox="0 0 250 512">
        <defs>
          <linearGradient id="dogTone" x1="0" y1="0" x2="0" y2="1">
            <stop offset="0" stop-color="var(--dog-dark)"/>
            <stop offset="0.5" stop-color="var(--dog-mid)"/>
            <stop offset="1" stop-color="var(--dog-light)"/>
          </linearGradient>
        </defs>
        <path d="M92 70 C92 20 130 0 170 0 C215 0 250 25 250 70 L250 500 C250 507 245 512 238 512 L12 512 C5 512 0 507 0 500 L0 200 C0 160 40 140 92 150 Z" fill="url(#dogTone)"/>
      </svg>
    </div>

    <ul class="features">
      <li>Premium Grade</li>
      <li>For Dental Health</li>
      <li>Grass-Fed Beef</li>
      <li>100% Digestible</li>
    </ul>

    <div class="size-note">
      <span class="size-num">6”</span>
      <span class="size-text">Bully<br>Sticks</span>
    </div>
  </main>
</body>
</html>
```